Stationary project for Velto Mobile Device training company
Stationary project for Velto Mobile Device training company - Electronics
Creative Brief
Use same font as used in my logo
Can use different fonts
Bright & Fun-filled
Dorian Welkett
PO Box 318 Medford, MA 02187
dorian@uPhaseMentor-example.com
www.uPhaseMentor-example.com

```html
<!DOCTYPE html>
<html lang="en">
<head>
<meta charset="utf-8">
<title>uPhase Mentor Stationery</title>
<link href="https://fonts.googleapis.com/css2?family=Exo+2:wght@400;600;700&display=swap" rel="stylesheet">
<style>
  :root{
    --bg:#e6e2dc;
    --paper:#ffffff;
    --paper-shade:#f1f1f1;
    --red:#d8262b;
    --red-dark:#a3161a;
    --charcoal:#2e2e30;
    --charcoal-deep:#1c1c1d;
    --grey:#6d6d70;
    --grey-light:#c9c9cb;
    --faint:#ececec;
    --caption:#5a534b;
  }
  *{box-sizing:border-box;margin:0;padding:0}
  html,body{width:1200px;height:634px;overflow:hidden;background:var(--bg)}
  body{font-family:"Exo 2",sans-serif;position:relative}
  .piece{position:absolute;box-shadow:0 3px 10px rgba(0,0,0,.28)}
  .caption{position:absolute;font-size:8px;color:var(--caption);font-family:"Exo 2",sans-serif;white-space:nowrap}

  .brand{display:flex;align-items:center;gap:6px}
  .brand-dot{border-radius:50%;background:var(--red);flex:none}
  .brand-name{font-weight:700;color:var(--charcoal);white-space:nowrap}
  .brand-tag{font-size:5px;color:var(--grey);letter-spacing:.5px;white-space:nowrap}

  /* letterhead */
  .letterhead{left:211px;top:36px;width:425px;height:571px;background:var(--paper)}
  .letterhead .brand{position:absolute;left:50%;top:34px;transform:translateX(-50%)}
  .letterhead .brand-dot{width:26px;height:26px}
  .letterhead .brand-name{font-size:15px}
  .letterhead .watermark{position:absolute;left:195px;top:150px;width:190px;height:190px;border-radius:50%;background:var(--faint)}
  .letterhead .rule{position:absolute;left:0;right:0;bottom:20px;height:2px;background:var(--red)}
  .letterhead .footer{position:absolute;left:0;right:0;bottom:0;height:20px;background:var(--charcoal);color:#ddd;font-size:5.5px;display:flex;align-items:center;justify-content:center;gap:10px;white-space:nowrap}

  /* front card */
  .card-front{left:48px;top:175px;width:235px;height:137px;background:var(--paper);overflow:hidden}
  .card-front .brand{position:absolute;left:14px;top:14px}
  .card-front .brand-dot{width:22px;height:22px}
  .card-front .brand-name{font-size:12px}
  .card-front .name-band{position:absolute;left:0;right:0;top:58px;height:18px;background:linear-gradient(var(--red),var(--red-dark));color:#fff;font-size:9px;font-weight:600;display:flex;align-items:center;justify-content:center}
  .card-front .details{position:absolute;left:0;right:0;top:76px;bottom:0;background:linear-gradient(var(--charcoal),var(--charcoal-deep));color:#ddd;font-size:5.5px;line-height:9px;display:flex;padding:12px 14px;gap:16px;white-space:nowrap}
  .card-front .divider{width:1px;background:var(--grey)}
  .contact-row{display:flex;align-items:center;gap:4px}
  .contact-row svg{width:7px;height:7px;fill:var(--red);flex:none}

  /* back card */
  .card-back{left:43px;top:365px;width:240px;height:144px;background:linear-gradient(135deg,#4a4a4c,var(--charcoal-deep));overflow:hidden}
  .card-back .disc{position:absolute;left:-20px;top:18px;width:110px;height:110px;border-radius:50%;background:radial-gradient(circle at 40% 40%,#5b5b5e,#1f1f20)}
  .card-back .brand{position:absolute;left:108px;top:60px;flex-direction:column;align-items:flex-start;gap:2px}
  .card-back .brand-name{font-size:14px;color:#fff}
  .card-back .brand-tag{color:var(--grey-light)}
  .card-back .edge{position:absolute;left:0;right:0;bottom:0;height:5px;background:var(--red)}

  /* envelopes */
  .envelope{overflow:hidden}
  .envelope svg.flap{position:absolute;left:0;top:0;width:100%;height:100%}
  .envelope .seal{position:absolute;left:50%;transform:translateX(-50%);display:flex;flex-direction:column;align-items:center;gap:3px}
  .envelope .seal .brand-dot{width:14px;height:14px}
  .envelope .seal .url{font-size:5px;white-space:nowrap}
  .env-dark{left:672px;top:36px;width:504px;height:216px;background:var(--paper-shade)}
  .env-dark .seal{top:40px}.env-dark .url{color:#ddd}
  .env-red{left:732px;top:132px;width:444px;height:216px;background:var(--paper-shade)}
  .env-red .seal{top:28px}.env-red .url{color:#fff}
  .env-white{left:720px;top:240px;width:456px;height:216px;background:var(--paper)}
  .env-white .seal{top:40px}.env-white .url{color:var(--grey)}

  .env-front{left:499px;top:422px;width:449px;height:166px;background:var(--paper)}
  .env-front .watermark{position:absolute;left:30px;top:8px;width:150px;height:150px;border-radius:50%;background:var(--faint)}
  .env-front .brand{position:absolute;left:18px;top:16px}
  .env-front .brand-dot{width:18px;height:18px}
  .env-front .brand-name{font-size:10px}
  .env-front .return{position:absolute;left:42px;top:40px;font-size:5px;color:var(--grey);white-space:nowrap}
  .env-front .rule{position:absolute;left:0;right:0;bottom:12px;height:2px;background:var(--red)}
  .env-front .base{position:absolute;left:0;right:0;bottom:0;height:12px;background:var(--charcoal)}
</style>
</head>
<body>

  <section class="piece envelope env-dark">
    <svg class="flap" viewBox="0 0 504 216" preserveAspectRatio="none" aria-hidden="true">
      <polygon points="0,0 504,0 504,20 252,120 0,20" fill="#2e2e30"/>
      <polyline points="0,216 252,120 504,216" fill="none" stroke="#dcdcdc" stroke-width="1"/>
    </svg>
    <div class="seal"><span class="brand-dot"></span><span class="url">www.uPhaseMentor-example.com</span></div>
  </section>

  <section class="piece envelope env-red">
    <svg class="flap" viewBox="0 0 444 216" preserveAspectRatio="none" aria-hidden="true">
      <polygon points="0,0 444,0 444,20 222,100 0,20" fill="#d8262b"/>
      <polyline points="0,216 222,100 444,216" fill="none" stroke="#dcdcdc" stroke-width="1"/>
    </svg>
    <div class="seal"><span class="brand-dot" style="background:var(--charcoal)"></span><span class="url">www.uPhaseMentor-example.com</span></div>
  </section>

  <section class="piece envelope env-white">
    <svg class="flap" viewBox="0 0 456 216" preserveAspectRatio="none" aria-hidden="true">
      <polygon points="0,0 456,0 456,20 228,112 0,20" fill="#fafafa" stroke="#dcdcdc"/>
      <polyline points="0,216 228,112 456,216" fill="none" stroke="#dcdcdc" stroke-width="1"/>
    </svg>
    <div class="seal"><span class="brand-dot"></span><span class="url">www.uPhaseMentor-example.com</span></div>
  </section>

  <section class="piece letterhead">
    <div class="watermark"></div>
    <div class="brand">
      <span class="brand-dot"></span>
      <div><div class="brand-name">uPhase Mentor</div><div class="brand-tag">MOBILE DEVICE TRAINING</div></div>
    </div>
    <div class="rule"></div>
    <div class="footer">
      <span>PO Box 318 Fenwold, QX 00918</span>
      <span>781-555-0147</span>
      <span>dorian@uPhaseMentor-example.com</span>
      <span>www.uPhaseMentor-example.com</span>
    </div>
  </section>

  <section class="piece env-front">
    <div class="watermark"></div>
    <div class="brand">
      <span class="brand-dot"></span>
      <div><div class="brand-name">uPhase Mentor</div><div class="brand-tag">MOBILE DEVICE TRAINING</div></div>
    </div>
    <div class="return">PO Box 318 Fenwold, QX 00918</div>
    <div class="rule"></div>
    <div class="base"></div>
  </section>

  <section class="piece card-front">
    <div class="brand">
      <span class="brand-dot"></span>
      <div><div class="brand-name">uPhase Mentor</div><div class="brand-tag">MOBILE DEVICE TRAINING</div></div>
    </div>
    <div class="name-band">Dorian Welkett</div>
    <div class="details">
      <div>PO Box 318<br>Fenwold, QX 00918</div>
      <div class="divider"></div>
      <div>
        <div class="contact-row"><svg viewBox="0 0 10 10"><path d="M2 1h2l1 2-1 1a6 6 0 0 0 2 2l1-1 2 1v2c0 1-1 1-1 1A8 8 0 0 1 1 2s0-1 1-1z"/></svg>781-555-0147</div>
        <div class="contact-row"><svg viewBox="0 0 10 10"><rect x="1" y="2" width="8" height="6"/></svg>781-555-0148</div>
        <div class="contact-row"><svg viewBox="0 0 10 10"><circle cx="5" cy="5" r="4"/></svg>dorian@uPhaseMentor-example.com</div>
      </div>
    </div>
  </section>
  <p class="caption" style="left:130px;top:322px">Front Card</p>

  <section class="piece card-back">
    <div class="disc"></div>
    <div class="brand">
      <div class="brand-name">uPhase Mentor</div>
      <div class="brand-tag">MOBILE DEVICE TRAINING</div>
    </div>
    <div class="edge"></div>
  </section>
  <p class="caption" style="left:110px;top:516px">Back Card Option 03</p>

  <p class="caption" style="left:380px;top:614px">Letterhead option 01</p>
  <p class="caption" style="left:1030px;top:592px">Envelope Front &amp; Back</p>

</body>
</html>
```